App Design for a petrol price in Nigeria

Through your already existing prototypes, we intend to design an app that would show petrol prices in Nigeria. The app would enable the user monitor the prices of petrol products in real time from nearby stations.

Industry/Entity Type

Gas And Oil

Requirements
Must have
• User community (sign up) and crowdsourced database integration

```html
<!DOCTYPE html>
<html lang="en">
<head>
<meta charset="utf-8">
<title>Pump Rates NG — Splash</title>
<link href="https://fonts.googleapis.com/css2?family=Inter:wght@600;700&display=swap" rel="stylesheet">
<style>
  :root {
    --brand-blue: #0A7BFF;
    --brand-green: #22F08E;
    --white: #FFFFFF;
  }
  * { margin: 0; padding: 0; box-sizing: border-box; }
  html, body {
    width: 1200px;
    height: 2596px;
    overflow: hidden;
  }
  body {
    background: var(--brand-blue);
    font-family: "Inter", Helvetica, Arial, sans-serif;
    color: var(--white);
    position: relative;
  }
  .status-bar {
    position: absolute;
    top: 0; left: 0;
    width: 1200px;
    height: 140px;
  }
  .status-time {
    position: absolute;
    left: 104px;
    top: 46px;
    font-size: 50px;
    font-weight: 600;
    letter-spacing: -0.5px;
  }
  .status-icons {
    position: absolute;
    right: 56px;
    top: 52px;
  }
  .splash-brand {
    position: absolute;
    left: 0;
    top: 1062px;
    width: 1200px;
    display: flex;
    flex-direction: column;
    align-items: center;
  }
  .brand-mark {
    width: 184px;
    height: 184px;
    border-radius: 44px;
    background: var(--brand-green);
  }
  .brand-name {
    margin-top: 66px;
    font-size: 68px;
    font-weight: 700;
    letter-spacing: 0.5px;
    line-height: 1;
  }
</style>
</head>
<body>
  <header class="status-bar">
    <span class="status-time">9:41</span>
    <svg class="status-icons" width="260" height="44" viewBox="0 0 260 44" aria-hidden="true">
      <g fill="#FFFFFF">
        <rect x="0" y="28" width="10" height="14" rx="2"/>
        <rect x="16" y="20" width="10" height="22" rx="2"/>
        <rect x="32" y="12" width="10" height="30" rx="2"/>
        <rect x="48" y="4" width="10" height="38" rx="2"/>
      </g>
      <g fill="none" stroke="#FFFFFF" stroke-width="6" stroke-linecap="round">
        <path d="M80 16 a34 34 0 0 1 48 0"/>
        <path d="M90 26 a20 20 0 0 1 28 0"/>
      </g>
      <circle cx="104" cy="37" r="5" fill="#FFFFFF"/>
      <rect x="150" y="4" width="90" height="38" rx="10" fill="none" stroke="#FFFFFF" stroke-opacity="0.5" stroke-width="3"/>
      <rect x="156" y="10" width="78" height="26" rx="6" fill="#FFFFFF"/>
      <rect x="244" y="16" width="6" height="14" rx="3" fill="#FFFFFF" fill-opacity="0.5"/>
    </svg>
  </header>

  <main class="splash-brand">
    <div class="brand-mark" aria-hidden="true"></div>
    <h1 class="brand-name">Pump Rates NG</h1>
  </main>
</body>
</html>
```